Commercial Loan Originator Business Card (CHANGE COLORS SCHEME)

CHANGE COLOR SCHEME - SAME DESIGN

Name Marissa Lantham
Title Commercial Loan Originator
Office (800) 641-2905 x68
Direct (240) 617-2435
Email brightleaf4you@mailpost.example

Name Derek Fallow
Office (800) 641-2905 x70
Direct (410) 932-1864
Email d.falthebroker@mailpost.example

Name Gordon Wexley
Office (800) 641-2905 x71
Direct (215) 346-2081
Email g.wexley37@mailpost.example

Name Lyn Moreau
Office (800) 641-2905 x
Direct (202) 458-1937
Email lmoreau64@mailpost.example

Name Nadia Strand
Office (800) 641-2905 x72
Direct (240) 871-5246
Email qrzhomelending@mailpost.example

```html
<!DOCTYPE html>
<html lang="en">
<head>
<meta charset="utf-8">
<title>Commercial Loan Originator Business Cards</title>
<link rel="stylesheet" href="https://fonts.googleapis.com/css2?family=Poppins:wght@400;500&family=Tinos:wght@400;700&display=swap">
<style>
  :root {
    --board-dark: #0b0b0b;
    --board-mid: #1f1f1f;
    --card-bg: #ffffff;
    --text-body: #3f3f46;
    --label-white: #f2f2f2;
    --accent-blue: #1e3fa0;
    --accent-purple: #a0279a;
    --accent-orange: #b35a22;
    --accent-pink: #e8348f;
    --accent-green: #2f4a40;
  }
  * { margin: 0; padding: 0; box-sizing: border-box; }
  html, body { width: 1189px; height: 1200px; overflow: hidden; }
  body {
    position: relative;
    background: radial-gradient(ellipse at 50% 45%, var(--board-mid) 0%, var(--board-dark) 75%);
    font-family: "Poppins", sans-serif;
  }
  .card-number {
    position: absolute;
    color: var(--label-white);
    font-size: 24px;
    font-weight: 400;
    line-height: 1;
  }
  .business-card {
    position: absolute;
    width: 500px;
    height: 286px;
    background: var(--card-bg);
    box-shadow: 0 6px 18px rgba(0,0,0,0.55);
    overflow: hidden;
  }
  .portrait {
    position: absolute;
    left: 53px;
    top: 59px;
    width: 168px;
    height: 168px;
    border-radius: 50%;
    border: 3px solid var(--accent);
  }
  .info {
    position: absolute;
    left: 273px;
    top: 72px;
    width: 218px;
    color: var(--text-body);
  }
  .name {
    color: var(--accent);
    font-size: 23px;
    font-weight: 500;
    line-height: 1.1;
    white-space: nowrap;
  }
  .title {
    font-size: 13px;
    line-height: 1.2;
    white-space: nowrap;
  }
  .rule {
    width: 52px;
    height: 2px;
    background: var(--accent);
    margin: 18px 0 36px;
  }
  .contact-list { list-style: none; font-size: 13px; line-height: 15.5px; }
  .contact-list li { display: flex; align-items: center; white-space: nowrap; }
  .contact-list svg { width: 9px; height: 9px; margin-right: 6px; fill: var(--accent); flex: none; }
  .contact-list .email-long { font-size: 11px; letter-spacing: -0.2px; }
  .card-serif .info { font-family: "Tinos", serif; }
  .card-serif .name { font-weight: 700; }
  .card-serif .title, .card-serif .contact-list { font-size: 12.5px; }
</style>
</head>
<body>
<svg width="0" height="0" style="position:absolute">
  <defs>
    <symbol id="icon-phone" viewBox="0 0 10 10"><path d="M1 3.2C1 2 2.5 1.2 5 1.2S9 2 9 3.2v.9H7V3H3v1.1H1zM2.3 4.6h5.4L8.8 8.6H1.2z"/></symbol>
    <symbol id="icon-mobile" viewBox="0 0 10 10"><path d="M2.5 0.5h5v9h-5zM3.6 1.6v6.8h2.8V1.6z"/></symbol>
    <symbol id="icon-mail" viewBox="0 0 10 10"><path d="M0.5 2h9v6h-9zM1.6 2.9 5 5.6 8.4 2.9v4.2H1.6z"/></symbol>
  </defs>
</svg>

<span class="card-number" style="left:34px;top:250px">1</span>
<span class="card-number" style="left:31px;top:581px">2</span>
<span class="card-number" style="left:31px;top:921px">3</span>
<span class="card-number" style="left:1147px;top:258px">4</span>
<span class="card-number" style="left:1147px;top:590px">5</span>

<article class="business-card" style="left:73px;top:126px;--accent:var(--accent-blue)">
  <div class="portrait" role="img" aria-label="Portrait photo of Gordon Wexley" style="background:radial-gradient(circle at 50% 40%, #6a4a3a 0%, #3a3f50 55%, #7f95ab 100%)"></div>
  <div class="info">
    <h2 class="name">Gordon Wexley</h2>
    <p class="title">Commercial Loan Originator</p>
    <div class="rule"></div>
    <ul class="contact-list">
      <li><svg><use href="#icon-phone"/></svg>(800) 641-2905 x71</li>
      <li><svg><use href="#icon-mobile"/></svg>(215) 346-2081</li>
      <li><svg><use href="#icon-mail"/></svg>g.wexley37@mailpost.example</li>
    </ul>
  </div>
</article>

<article class="business-card" style="left:605px;top:126px;width:503px;height:288px;--accent:var(--accent-purple)">
  <div class="portrait" role="img" aria-label="Portrait photo of Lyn Moreau" style="background:radial-gradient(circle at 50% 45%, #7a5040 0%, #a86a5e 50%, #4d7a45 100%)"></div>
  <div class="info">
    <h2 class="name">Lyn Moreau</h2>
    <p class="title">Commercial Loan Originator</p>
    <div class="rule"></div>
    <ul class="contact-list">
      <li><svg><use href="#icon-phone"/></svg>(800) 641-2905 x</li>
      <li><svg><use href="#icon-mobile"/></svg>(202) 458-1937</li>
      <li><svg><use href="#icon-mail"/></svg>lmoreau64@mailpost.example</li>
    </ul>
  </div>
</article>

<article class="business-card" style="left:73px;top:459px;height:284px;--accent:var(--accent-orange)">
  <div class="portrait" role="img" aria-label="Portrait photo of Nadia Strand" style="background:radial-gradient(circle at 50% 45%, #8a5a3e 0%, #6e4a36 50%, #a17d63 100%)"></div>
  <div class="info">
    <h2 class="name">Nadia Strand</h2>
    <p class="title">Commercial Loan Originator</p>
    <div class="rule"></div>
    <ul class="contact-list">
      <li><svg><use href="#icon-phone"/></svg>(800) 641-2905 x72</li>
      <li><svg><use href="#icon-mobile"/></svg>(240) 871-5246</li>
      <li class="email-long"><svg><use href="#icon-mail"/></svg>qrzhomelending@mailpost.example</li>
    </ul>
  </div>
</article>

<article class="business-card card-serif" style="left:603px;top:456px;width:504px;height:288px;--accent:var(--accent-green)">
  <div class="portrait" role="img" aria-label="Portrait photo of Derek Fallow" style="background:radial-gradient(circle at 50% 40%, #5a3e30 0%, #35352f 55%, #b9bcc0 100%)"></div>
  <div class="info">
    <h2 class="name">Derek Fallow</h2>
    <p class="title">Commercial Loan Originator</p>
    <div class="rule"></div>
    <ul class="contact-list">
      <li><svg><use href="#icon-phone"/></svg>(800) 641-2905 x70</li>
      <li><svg><use href="#icon-mobile"/></svg>(410) 932-1864</li>
      <li><svg><use href="#icon-mail"/></svg>d.falthebroker@mailpost.example</li>
    </ul>
  </div>
</article>

<article class="business-card" style="left:73px;top:789px;height:285px;--accent:var(--accent-pink)">
  <div class="portrait" role="img" aria-label="Portrait photo of Marissa Lantham" style="background:radial-gradient(circle at 50% 45%, #8b5e48 0%, #c9a08c 45%, #f2f2f2 75%, #e86aa8 100%)"></div>
  <div class="info">
    <h2 class="name">Marissa Lantham</h2>
    <p class="title">Commercial Loan Originator</p>
    <div class="rule"></div>
    <ul class="contact-list">
      <li><svg><use href="#icon-phone"/></svg>(800) 641-2905 x68</li>
      <li><svg><use href="#icon-mobile"/></svg>(240) 617-2435</li>
      <li class="email-long"><svg><use href="#icon-mail"/></svg>brightleaf4you@mailpost.example</li>
    </ul>
  </div>
</article>
</body>
</html>
```